Covid 19 Exit Strategy one page brochure

I would like to design, and will need URGENT help, a brochure detailing a Covid 19 Exit Strategy plan. This brochure will need to be understood easily and the graphics inside should make it easy for people to understand without reading the entire text. This project is quite urgent and needs to be completed THIS WEEK - by Saturday may 16th at the latest. I am attaching two examples. I will provide the text.

```html
<!DOCTYPE html>
<html lang="en">
<head>
<meta charset="utf-8">
<title>COVID-19 Phased Exit Strategy</title>
<link rel="stylesheet" href="https://fonts.googleapis.com/css2?family=Arimo:wght@400;700&display=swap">
<style>
:root{
  --red:#d7231f;
  --ink:#111;
  --white:#fff;
  --photo-light:#d9d9d9;
  --photo-mid:#9a9a9a;
  --photo-dark:#3a3a3a;
  --surgical:#7fa7b8;
}
*{box-sizing:border-box;margin:0;padding:0}
html,body{width:848px;height:1200px;overflow:hidden;background:var(--white)}
.brochure{
  position:relative;width:848px;height:1200px;overflow:hidden;
  font-family:"Arimo",Arial,sans-serif;color:var(--ink);
  background:linear-gradient(180deg,var(--white) 0,var(--white) 610px,#cfcfcf 800px,#6e6e6e 1000px,#0c0c0c 1200px);
}
.hero-photo{
  position:absolute;left:0;top:0;width:848px;height:380px;
  background:
    linear-gradient(180deg,rgba(255,255,255,0) 55%,var(--white) 100%),
    linear-gradient(90deg,#f4f4f4 0%,var(--photo-light) 40%,#bdbdbd 70%,#e8e8e8 100%);
}
.title-box{
  position:absolute;left:53px;top:50px;width:545px;height:78px;
  background:linear-gradient(90deg,var(--white) 70%,rgba(255,255,255,.6));
  text-align:center;color:var(--red);
}
.title-box .kicker{display:block;margin-left:150px;font-size:24px;font-weight:700;line-height:30px;padding-top:6px}
.title-box .headline{display:block;margin-left:150px;font-size:31px;font-weight:400;line-height:36px}
.credit{position:absolute;left:41px;top:140px;font-size:11.5px;font-weight:700}
.intro{
  position:absolute;left:80px;top:160px;width:726px;
  font-size:13.6px;line-height:15.2px;text-align:justify;text-indent:20px;
}
.section-label{
  position:absolute;left:53px;top:378px;width:275px;height:25px;background:var(--white);
  padding:4px 0 0 5px;font-size:16px;color:var(--red);
}
.requirements{
  position:absolute;left:20px;top:410px;width:784px;
  list-style:none;counter-reset:req;font-size:13.6px;line-height:15.2px;
}
.requirements li{position:relative;padding-left:19px;margin-bottom:3px;counter-increment:req}
.requirements li::before{content:counter(req) ".";position:absolute;left:0}
.circle-photo{
  position:absolute;left:449px;top:692px;width:356px;height:356px;border-radius:50%;
  background:radial-gradient(circle at 45% 40%,#e4e4e4 0,#a8a8a8 45%,#4a4a4a 100%);
}
.surgery-photo{
  position:absolute;left:0;top:872px;width:435px;height:328px;
  background:linear-gradient(160deg,#9fb3bd 0%,var(--surgical) 40%,#2f5a55 85%,#1e3a36 100%);
}
</style>
</head>
<body>
<main class="brochure">
  <div class="hero-photo" role="img" aria-label="Faded black and white photo of healthcare workers in protective gowns and face shields"></div>

  <header class="title-box">
    <span class="kicker">COVID-19</span>
    <h1 class="headline">Phased Exit Strategy</h1>
  </header>

  <p class="credit">Developed by Lena Varrow</p>

  <p class="intro">Pandemics have, historically, seen their end both medically - via herd immunity or immunizations. And while there are several clinical trials underway for potential Covid-19 vaccines, we are still a long way from deploying an effective vaccine and one that will stand the test of time as the virus changes. Covid-19 pandemic will be considered ‘ended’ when there are only occasional traces of localized cases that are quickly contained in specific locations., Today and in the absence of an effective vaccine(s) and for the re-opening of the economies and social activities to be successful, it is critical that the following basic conditions be in place before any lockdowns are lifted and before social activities resume:</p>

  <h2 class="section-label">General requirements:</h2>

  <ol class="requirements">
    <li>Single digit downward trend of documented cases within the past 14-days.</li>
    <li>Hospitals and the health care system are capable of treating patients without operating on a crisis mode.</li>
    <li>Ability to screen and test symptomatic individuals within 24 hours of identification. Increased and sufficient testing capacity, to test at least 50% of all population if necessary within a timeframe of 3 months.</li>
    <li>Ability to surge ICU capacity on a short notice - 24h.</li>
    <li>Ability to track and trace infected patients and contacts on a live basis and across the country and ability to react quickly to any unusual trends or outbreaks.</li>
    <li>Plan in place to trigger targeted or full-scale containment in case of sudden outbreaks</li>
    <li>Mandatory use of masks (at least surgical grade) for everyone in all public areas and at work. Mandatory use of N95, or equivalent, masks for all healthcare front workers and for all government agencies and authorities that are involved in overseeing the containment activities.</li>
    <li>Mandatory daily checks of body temperature for everyone at the workplace or entering public areas.</li>
    <li>Mandatory sanitation in all places - use of disinfection available on a large scale.</li>
  </ol>

  <div class="circle-photo" role="img" aria-label="Black and white photo of two healthcare workers in protective gear embracing"></div>
  <div class="surgery-photo" role="img" aria-label="Photo of a medical worker in a face shield and mask inside an operating room"></div>
</main>
</body>
</html>
```